Infographic for a Life Transformation brand to showcase their principle method

I need a clean infographic which would be used in a brochure to show the 5 steps to achieving a Quiet Harvest. (ie Life transformation). I use the theme of a revolution so I would like the graphic to include a raised fist or something to represent a revolution and then the 5 points of information to represent each step.
Needs to very clean and simple. I don't want something that would take up a full page, I want it as a graphic, almost like a big logo. I don't want it laid out like a process chart.

My brand personalities from https://tonequirkhub.com.au/ are
The Everyman and The Magician to give you an idea of my brand.

I've attached my logo so that you can see the colour of it. Graphic doesn't need to match logo but should align with that colour.

Target Market(s)

Top Tier Executives, males, 35-55y old

Industry/Entity Type

Life Coaching

Requirements
Must have
• The graphic must have the 5 Steps: in this order
1.Clarity
2. Measurement
3. Discipline
4. Nutrition
5.Exercise
Nice to have
• It could include these action steps which line up with the 5 steps, It may be too much information by there is the option to include if it works.
1.see it
2. track it
3. do it
4. eat it
5. move it

```html
<!DOCTYPE html>
<html lang="en">
<head>
<meta charset="utf-8">
<title>Quiet Harvest – Five Steps</title>
<link rel="stylesheet" href="https://fonts.googleapis.com/css2?family=Oswald:wght@300;500&family=Poppins:wght@500&display=swap">
<style>
  :root {
    --brand-blue: #0b4c92;
    --clarity: #ab4b85;
    --measurement: #ec7324;
    --discipline: #00a0e0;
    --nutrition: #86b22f;
    --exercise: #e31e25;
    --action-grey: #3d3d3d;
    --paper: #ffffff;
  }
  html, body {
    margin: 0;
    padding: 0;
    width: 1200px;
    height: 1200px;
    overflow: hidden;
    background: var(--paper);
  }
  .infographic {
    display: block;
    width: 1200px;
    height: 1200px;
  }
  .brand-mark { fill: var(--brand-blue); }
  .brand-name {
    font-family: "Poppins", sans-serif;
    font-weight: 500;
    font-size: 50px;
    letter-spacing: 0.34em;
    fill: var(--brand-blue);
  }
  .step-title {
    font-family: "Oswald", sans-serif;
    font-weight: 500;
    font-size: 62px;
  }
  .step-action {
    font-family: "Oswald", sans-serif;
    font-weight: 300;
    font-size: 54px;
    fill: var(--action-grey);
  }
  .leader { fill: none; stroke-width: 3; }
  .icon { fill: none; stroke: var(--paper); stroke-width: 4; stroke-linecap: round; stroke-linejoin: round; }
  .icon-fill { fill: var(--paper); }

  .step--clarity .segment { fill: var(--clarity); }
  .step--clarity .step-title { fill: var(--clarity); }
  .step--clarity .leader { stroke: var(--clarity); }

  .step--measurement .segment { fill: var(--measurement); }
  .step--measurement .step-title { fill: var(--measurement); }
  .step--measurement .leader { stroke: var(--measurement); }

  .step--discipline .segment { fill: var(--discipline); }
  .step--discipline .step-title { fill: var(--discipline); }
  .step--discipline .leader { stroke: var(--discipline); }

  .step--nutrition .segment { fill: var(--nutrition); }
  .step--nutrition .step-title { fill: var(--nutrition); }
  .step--nutrition .leader { stroke: var(--nutrition); }

  .step--exercise .segment { fill: var(--exercise); }
  .step--exercise .step-title { fill: var(--exercise); }
  .step--exercise .leader { stroke: var(--exercise); }
</style>
</head>
<body>
<svg class="infographic" viewBox="0 0 1200 1200" xmlns="http://www.w3.org/2000/svg" role="img" aria-label="Quiet Harvest: five steps – Clarity, Measurement, Discipline, Nutrition, Exercise">

  <g class="brand">
    <rect class="brand-mark" x="548" y="150" width="106" height="106"/>
    <text class="brand-name" x="610" y="390" text-anchor="middle">QUIET HARVEST</text>
  </g>

  <g class="step step--clarity">
    <path class="segment" d="M350.7 1084.1 A270 270 0 0 1 348.9 886.2 L473.1 933.9 A137 137 0 0 0 474.0 1034.3 Z"/>
    <g class="icon">
      <circle cx="398" cy="985" r="30"/>
      <path d="M376 987 Q398 967 420 987 Q398 1005 376 987 Z"/>
      <circle cx="398" cy="987" r="6"/>
    </g>
    <path class="leader" d="M142 952 H305 L332 979"/>
    <text class="step-title" x="226" y="1019" text-anchor="middle" textLength="141" lengthAdjust="spacingAndGlyphs">CLARITY</text>
    <text class="step-action" x="227" y="1066" text-anchor="middle" textLength="98" lengthAdjust="spacingAndGlyphs">(SEE IT)</text>
  </g>

  <g class="step step--measurement">
    <path class="segment" d="M352.5 877.5 A270 270 0 0 1 491.2 736.4 L545.3 857.9 A137 137 0 0 0 474.9 929.5 Z"/>
    <g class="icon" transform="rotate(-45 456 841)">
      <rect x="420" y="842" width="74" height="26"/>
      <path d="M430 842 v10 M440 842 v7 M450 842 v10 M460 842 v7 M470 842 v10 M480 842 v7"/>
      <path d="M422 826 H492 M422 826 l8 -6 M422 826 l8 6 M492 826 l-8 -6 M492 826 l-8 6"/>
    </g>
    <path class="leader" d="M132 728 H382 L431 776"/>
    <text class="step-title" x="255" y="800" text-anchor="middle" textLength="257" lengthAdjust="spacingAndGlyphs">MEASUREMENT</text>
    <text class="step-action" x="257" y="853" text-anchor="middle" textLength="132" lengthAdjust="spacingAndGlyphs">(TRACK IT)</text>
  </g>

  <g class="step step--discipline">
    <path class="segment" d="M499.9 732.7 A270 270 0 0 1 702.1 732.7 L652.3 856.0 A137 137 0 0 0 549.7 856.0 Z"/>
    <g class="icon">
      <rect x="574" y="750" width="54" height="66" rx="5"/>
      <rect x="589" y="744" width="24" height="11" rx="3"/>
      <path d="M586 774 H616 M586 790 H616 M586 806 H616"/>
    </g>
    <path class="leader" d="M503 650 H699 M601 650 V713"/>
    <text class="step-title" x="601" y="583" text-anchor="middle" textLength="187" lengthAdjust="spacingAndGlyphs">DISCIPLINE</text>
    <text class="step-action" x="601" y="634" text-anchor="middle" textLength="84" lengthAdjust="spacingAndGlyphs">(DO IT)</text>
  </g>

  <g class="step step--nutrition">
    <path class="segment" d="M710.8 736.4 A270 270 0 0 1 849.5 877.5 L727.1 929.5 A137 137 0 0 0 656.7 857.9 Z"/>
    <g class="icon">
      <path d="M746 866 C716 848 714 826 728 818 C738 812 746 820 746 826 C746 820 754 812 764 818 C778 826 776 848 746 866 Z"/>
      <path d="M738 838 Q746 831 754 838 M742 844 Q746 841 750 844"/>
    </g>
    <path class="leader" d="M1061 728 H810 L766 774"/>
    <text class="step-title" x="943" y="800" text-anchor="middle" textLength="182" lengthAdjust="spacingAndGlyphs">NUTRITION</text>
    <text class="step-action" x="943" y="853" text-anchor="middle" textLength="94" lengthAdjust="spacingAndGlyphs">(EAT IT)</text>
  </g>

  <g class="step step--exercise">
    <path class="segment" d="M853.1 886.2 A270 270 0 0 1 851.3 1084.1 L728.0 1034.3 A137 137 0 0 0 728.9 933.9 Z"/>
    <g class="icon">
      <path d="M770 1005 H830 M776 1005 v9 M824 1005 v9"/>
      <path d="M820 1005 L836 966 L826 955"/>
      <circle class="icon-fill" cx="770" cy="1005" r="5"/>
      <circle class="icon-fill" cx="830" cy="1005" r="5"/>
    </g>
    <path class="leader" d="M1054 952 H892 L870 976"/>
    <text class="step-title" x="974" y="1019" text-anchor="middle" textLength="160" lengthAdjust="spacingAndGlyphs">EXERCISE</text>
    <text class="step-action" x="975" y="1066" text-anchor="middle" textLength="120" lengthAdjust="spacingAndGlyphs">(MOVE IT)</text>
  </g>
</svg>
</body>
</html>
```